TWS Business Card Design

As a full service media and advocacy firm, we lean on years of experience in political and corporate consulting, grassroots campaigning, media placement, and video production to deliver unparalleled results. Recently we have moved into digital media and now provide this service for our clients.

I will add our two company logos to be used on the business cards. The longer logo with "sky reach studio" is our primary logo. Our secondary logo is more square one with "sky reach" and 'digital.media.campaigns" on it. We are looking for clean and modern looking business cards fitting for a digital firm.

I will also add our logos that go well with dark backgrounds.

Industry/Entity Type

Political

Contact Information for Business Card

Denton Pratchard, Director of Campaigns and Digital, 571-482-7165, denton@skyreachstudioco.com, @SkyReachStudioCo, @DentonPratchard, Facebook.com/SkyReachStudioCo

```html
<!DOCTYPE html>
<html lang="en">
<head>
<meta charset="utf-8">
<title>Sky Reach Studio – Business Card</title>
<link rel="stylesheet" href="https://fonts.googleapis.com/css2?family=Open+Sans:wght@700&family=Carlito:wght@700&display=swap">
<style>
  :root {
    --band-lavender: #a7b2e4;
    --band-light: #d3e5f5;
    --steel-edge: #a3a3a3;
    --steel-light: #ececec;
    --steel-shade: #8f8f8f;
    --brand-blue: #5294cc;
    --ink: #0d0d0d;
  }
  * { margin: 0; padding: 0; box-sizing: border-box; }
  html, body { width: 1200px; height: 720px; overflow: hidden; background: #ffffff; }
  .card { position: relative; width: 1200px; height: 720px; overflow: hidden; }

  .band-top, .band-bottom {
    position: absolute; left: 0; width: 1200px;
    background: linear-gradient(100deg, var(--band-lavender) 0%, var(--band-light) 45%, var(--band-light) 55%, var(--band-lavender) 100%);
  }
  .band-top { top: 0; height: 214px; }
  .band-bottom { top: 525px; height: 195px; }

  .band-steel {
    position: absolute; left: 0; top: 214px; width: 1200px; height: 311px;
    background: linear-gradient(90deg, var(--steel-edge) 0%, #d4d4d4 35%, var(--steel-light) 55%, #d0d0d0 80%, var(--steel-edge) 100%);
  }

  .tail { position: absolute; }
  .tail--top-right { left: 1018px; top: 214px; width: 140px; height: 72px; }
  .tail--bottom-left { left: 50px; top: 525px; width: 144px; height: 74px; }

  .wordmark {
    position: absolute; font-family: "Open Sans", sans-serif; font-weight: 700;
    color: var(--brand-blue); white-space: nowrap; line-height: 1;
  }
  .wordmark--primary { left: 0; width: 1200px; top: 42px; text-align: center; font-size: 104px; letter-spacing: 1px; }
  .wordmark--secondary { left: 120px; width: 460px; top: 580px; text-align: center; font-size: 60px; }

  .person-name {
    position: absolute; left: 8px; top: 318px;
    font-family: "Open Sans", sans-serif; font-weight: 700; font-size: 58px;
    color: var(--ink); white-space: nowrap; line-height: 1;
  }

  .contact, .social {
    position: absolute; left: 612px;
    font-family: "Carlito", sans-serif; font-weight: 700; font-size: 35px;
    color: var(--ink); list-style: none; line-height: 1;
  }
  .contact { top: 300px; }
  .contact li { height: 52px; }
  .contact li + li { margin-top: 0; }
  .social { top: 570px; }
  .social li { height: 58px; }
</style>
</head>
<body>
<main class="card">
  <div class="band-top"></div>
  <div class="band-steel"></div>
  <div class="band-bottom"></div>

  <svg class="tail tail--top-right" viewBox="0 0 140 72" aria-hidden="true">
    <polygon points="0,0 140,0 70,72" fill="var(--steel-shade)" opacity="0.35"/>
    <polyline points="0,0 70,72 140,0" fill="none" stroke="#7f7f7f" stroke-width="2"/>
  </svg>
  <svg class="tail tail--bottom-left" viewBox="0 0 144 74" aria-hidden="true">
    <polygon points="0,0 144,0 72,74" fill="#a9a9a9"/>
  </svg>

  <div class="wordmark wordmark--primary">sky reach studio</div>

  <h1 class="person-name">Denton Pratchard</h1>

  <ul class="contact">
    <li>Director of Campaigns and Digital</li>
    <li>571-482-7165</li>
    <li>denton@skyreachstudioco.com</li>
    <li>@DentonPratchard</li>
  </ul>

  <div class="wordmark wordmark--secondary">sky reach</div>

  <ul class="social">
    <li>@SkyReachStudioCo</li>
    <li>Facebook.com/SkyReachStudioCo</li>
  </ul>
</main>
</body>
</html>
```